Criação de Embalagem (unidade) para Roupas, Jóias & acessórios
A empresa queria:
" Venda de roupas femininas 90% e no futuro, masculinas. Público adulto. Roupas casuais, estilo jovem. Classe média. "

```html
<!DOCTYPE html>
<html lang="pt">
<head>
<meta charset="utf-8">
<title>Velora Modas – Sacola</title>
<link rel="stylesheet" href="https://fonts.googleapis.com/css2?family=Raleway:wght@300&display=swap">
<style>
  :root {
    --backdrop: #cfccc5;
    --bag-top: #55283a;
    --bag-bottom: #241a1f;
    --pattern-top: #6e3446;
    --pattern-bottom: #3a2029;
    --stripe-top: #e8457f;
    --stripe-mid: #f08a7a;
    --stripe-bottom: #f3e48a;
    --brand-ink: #f1dede;
    --accent: #e9828a;
  }
  html, body {
    margin: 0;
    padding: 0;
    width: 1200px;
    height: 1200px;
    overflow: hidden;
    background: var(--backdrop);
  }
  .canvas {
    width: 1200px;
    height: 1200px;
    display: block;
  }
  .brand-name {
    font-family: "Raleway", sans-serif;
    font-weight: 300;
    fill: var(--brand-ink);
  }
</style>
</head>
<body>
<svg class="canvas" viewBox="0 0 1200 1200" xmlns="http://www.w3.org/2000/svg">
  <defs>
    <linearGradient id="bag-fill" x1="0" y1="0" x2="0" y2="1">
      <stop offset="0" stop-color="var(--bag-top)"/>
      <stop offset="1" stop-color="var(--bag-bottom)"/>
    </linearGradient>
    <linearGradient id="pattern-fill" x1="0" y1="0" x2="0" y2="1">
      <stop offset="0" stop-color="var(--pattern-top)"/>
      <stop offset="1" stop-color="var(--pattern-bottom)"/>
    </linearGradient>
    <linearGradient id="stripe-fill" x1="0" y1="0" x2="0" y2="1">
      <stop offset="0" stop-color="var(--stripe-top)"/>
      <stop offset="0.5" stop-color="var(--stripe-mid)"/>
      <stop offset="1" stop-color="var(--stripe-bottom)"/>
    </linearGradient>
  </defs>

  <g class="bag">
    <rect class="bag-body" x="280" y="80" width="640" height="1040" fill="url(#bag-fill)"/>

    <rect class="side-pattern" x="280" y="80" width="170" height="1040"
          fill="url(#pattern-fill)" role="img"
          aria-label="Padrão decorativo de losangos com pontos em tons rosados"/>

    <rect class="accent-stripe" x="456" y="80" width="11" height="1040" fill="url(#stripe-fill)"/>

    <rect class="handle-cutout" x="545" y="225" width="100" height="36" rx="18"
          fill="var(--backdrop)"/>

    <g class="brand">
      <text class="brand-name brand-wordmark" transform="translate(715 790) rotate(-90)"
            font-size="66" letter-spacing="12">VELORA</text>
      <text class="brand-name brand-tagline" transform="translate(748 490) rotate(90)"
            font-size="22" letter-spacing="16">MODAS</text>
      <circle class="brand-dot" cx="692" cy="835" r="12" fill="var(--accent)"/>
    </g>
  </g>
</svg>
</body>
</html>
```